New Business Card Design Project

Easy part first... I want the backside to be simple... jet black background with our logo in jet black/white/color. Feel free to play with tagline ideas under the logo if you want, I'm still toying around with it myself.

The front side... I need the logo on it, my photo headshot, and the following information:

Ray T. Calloway
Top Producer
555-201-4837
calloway.ray.t@fernmail.example
www.listnorthernnests.example
www.getnorthernnests.example

I'm looking for creativity with font, simple, but elegant, pairs well with the logo, good visibility of my photo, black background on the front as well, clearly see and identify information.
Updates

I would like the websites to have capitalization on the first letter of each word - www.ListNorthernNests.example and www.GetNorthernNests.example Also, I would like each of the capital letters to be slightly larger than the other font

Target Market(s)

We help people buy and sell homes from $50,000 to over a $1million.

Industry/Entity Type

Business

Requirements
Must have
• Must have information from above.
Nice to have
• Introducing a new color to be sharp against the black- possibly in the silver/nickel/platinum metallics? Feel free to crop the headshot down some if needed.
Should not have
• NO CHEESY GRAPHICS

```html
<!DOCTYPE html>
<html lang="en">
<head>
<meta charset="utf-8">
<title>Hearthway Realty — Business Card</title>
<link rel="stylesheet" href="https://fonts.googleapis.com/css2?family=Cinzel:wght@400;600&family=Share+Tech+Mono&display=swap">
<style>
  :root {
    --backdrop: #1b1b1d;
    --card-black: #0c0c0d;
    --card-edge: #26262a;
    --silver: #d4d5d8;
    --silver-dim: #a9abb0;
    --photo-dark: #2a2c31;
    --photo-mid: #6f6a66;
    --photo-light: #b39b8c;
  }
  * { box-sizing: border-box; margin: 0; padding: 0; }
  html, body {
    width: 1200px;
    height: 994px;
    overflow: hidden;
    background: var(--backdrop);
  }
  .canvas {
    width: 1200px;
    height: 994px;
    display: flex;
    align-items: center;
    justify-content: center;
    gap: 40px;
  }
  .card {
    position: relative;
    width: 540px;
    height: 309px;
    background: var(--card-black);
    border: 1px solid var(--card-edge);
    border-radius: 6px;
    overflow: hidden;
    box-shadow: 0 14px 30px rgba(0,0,0,0.45);
  }

  /* Brand lockup (name only) */
  .brand {
    display: flex;
    align-items: center;
    gap: 10px;
    color: var(--silver);
    font-family: "Cinzel", Georgia, serif;
    font-weight: 600;
    letter-spacing: 0.06em;
  }
  .brand-square {
    width: 14px;
    height: 14px;
    background: var(--silver);
    flex: none;
  }

  /* Front */
  .card-front .brand {
    position: absolute;
    top: 34px;
    right: 34px;
    font-size: 22px;
  }
  .headshot {
    position: absolute;
    left: 0;
    bottom: 0;
    width: 232px;
    height: 200px;
    background: linear-gradient(160deg, var(--photo-light) 0%, var(--photo-mid) 38%, var(--photo-dark) 100%);
  }
  .contact {
    position: absolute;
    right: 34px;
    top: 92px;
    width: 250px;
    color: var(--silver);
    font-family: "Share Tech Mono", "Courier New", monospace;
    text-align: left;
  }
  .contact-name {
    font-family: "Cinzel", Georgia, serif;
    font-weight: 400;
    font-size: 19px;
    letter-spacing: 0.08em;
  }
  .contact-title {
    font-family: "Cinzel", Georgia, serif;
    font-size: 12px;
    letter-spacing: 0.12em;
    color: var(--silver-dim);
    margin-top: 3px;
    margin-bottom: 22px;
  }
  .contact-line {
    font-size: 12.5px;
    letter-spacing: 0.04em;
    line-height: 1.75;
  }
  .contact-line .cap { font-size: 14.5px; }

  /* Back */
  .card-back {
    display: flex;
    flex-direction: column;
    align-items: center;
    justify-content: center;
  }
  .card-back .brand {
    font-size: 34px;
    gap: 14px;
  }
  .card-back .brand-square { width: 20px; height: 20px; }
  .back-rule {
    width: 250px;
    height: 1px;
    margin-top: 14px;
    background: linear-gradient(90deg, transparent, var(--silver), transparent);
  }
</style>
</head>
<body>
  <main class="canvas">
    <section class="card card-front" aria-label="Front of business card">
      <div class="brand"><span class="brand-square"></span>Hearthway Realty</div>
      <div class="headshot" role="img" aria-label="Headshot photo of the agent in a dark suit and blue tie"></div>
      <div class="contact">
        <p class="contact-name">Ray T. Calloway</p>
        <p class="contact-title">Top Producer</p>
        <p class="contact-line">555-201-4837</p>
        <p class="contact-line">calloway.ray.t@fernmail.example</p>
        <p class="contact-line">www.<span class="cap">L</span>ist<span class="cap">N</span>orthern<span class="cap">N</span>ests.example</p>
        <p class="contact-line">www.<span class="cap">G</span>et<span class="cap">N</span>orthern<span class="cap">N</span>ests.example</p>
      </div>
    </section>

    <section class="card card-back" aria-label="Back of business card">
      <div class="brand"><span class="brand-square"></span>Hearthway Realty</div>
      <div class="back-rule"></div>
    </section>
  </main>
</body>
</html>
```